Equity, Effectiveness and Efficiency in charitable food relief sector

I am undertaking my PhD in food policy in the charitable food relief sector, specifically investigating the factors (supply, demand and capacity) that affect the introduction of nutrition policy and in turn, affect the sector's ability to achieve equity, effectiveness and efficiency.

I need a graphic device that incorporates this central idea of Equity, Effectiveness and Efficiency, and how the factors of supply, demand and capacity interact. There are sub-factors within supply (1-6), demand (7-10) and capacity (11 - 15). All these details are shown in the attached figure (Basic figure_Eq Effec Effic and factors.jpg)

This figure (Basic figure_Eq Effec Effic and factors.jpg) contains all the information I need in a graphic but I need something that is more visually appealing, and that can link the ideas in a format other than a table. The final graphic will outline how the food relief sector balances the core objectives of equity, effectiveness and efficiency with the factors (and sub-factors) of supply, demand and capacity.

```html
<!DOCTYPE html>
<html lang="en">
<head>
<meta charset="utf-8">
<title>Factors Affecting the Introduction of Nutrition Policy</title>
<link rel="stylesheet" href="https://fonts.googleapis.com/css2?family=Arimo:wght@400;700&display=swap">
<style>
  :root {
    --ink: #000000;
    --paper: #ffffff;
    --guide: #b0c0bf;
    --supply: #fd99c9;
    --demand: #89c589;
    --capacity: #9acbcb;
    --core: #eb5220;
    --core-text: #ffffff;
  }
  html, body {
    margin: 0;
    padding: 0;
    width: 1200px;
    height: 1200px;
    overflow: hidden;
    background: var(--paper);
  }
  .factor-diagram {
    display: block;
    width: 1200px;
    height: 1200px;
    font-family: "Arimo", Arial, sans-serif;
  }
  .guide-arc, .guide-line, .core-ring {
    fill: none;
    stroke: var(--guide);
    stroke-width: 7;
    stroke-linecap: round;
  }
  .sector { stroke: var(--guide); stroke-width: 3; }
  .sector--supply { fill: var(--supply); }
  .sector--demand { fill: var(--demand); }
  .sector--capacity { fill: var(--capacity); }
  .core-gap { fill: var(--paper); }
  .core-disc { fill: var(--core); }
  .diagram-title {
    font-size: 47px;
    font-weight: 700;
    fill: var(--ink);
    text-anchor: middle;
  }
  .sector-heading {
    font-size: 51px;
    font-weight: 700;
    fill: var(--ink);
    text-decoration: underline;
  }
  .factor-item {
    font-size: 40px;
    fill: var(--ink);
  }
  .factor-item .num { font-weight: 700; }
  .core-label {
    fill: var(--core-text);
    font-weight: 700;
    text-anchor: middle;
  }
  .core-label--equity { font-size: 56px; }
  .core-label--effectiveness { font-size: 39px; }
  .core-label--efficiency { font-size: 44px; }
</style>
</head>
<body>
<svg class="factor-diagram" viewBox="0 0 1932 1932" xmlns="http://www.w3.org/2000/svg" role="img" aria-label="Factors affecting the introduction of nutrition policy: supply, demand and capacity around equity, effectiveness and efficiency">

  <text class="diagram-title" x="966" y="230">FACTSORS AFFECTING THE INTRODUCTION</text>
  <text class="diagram-title" x="966" y="287">OF NUTRITION POLICY</text>

  <!-- guide arcs -->
  <path class="guide-arc" d="M1631.2 370.9 A850 850 0 1 1 292.6 381.8"/>
  <path class="guide-arc" d="M1414.3 317.6 A735 735 0 1 1 513.5 320.8"/>
  <path class="guide-arc" d="M1467.4 728.3 A530 530 0 1 1 589.3 527.3"/>

  <!-- guide lines -->
  <line class="guide-line" x1="914" y1="707" x2="820" y2="350"/>
  <line class="guide-line" x1="1108" y1="758" x2="1516" y2="345"/>
  <line class="guide-line" x1="773" y1="847" x2="200" y2="688"/>
  <line class="guide-line" x1="824" y1="1041" x2="265" y2="1595"/>
  <line class="guide-line" x1="1166" y1="893" x2="1885" y2="893"/>
  <line class="guide-line" x1="1018" y1="1093" x2="1200" y2="1768"/>

  <circle class="core-ring" cx="966" cy="900" r="200"/>

  <!-- sectors -->
  <path class="sector sector--demand" d="M966 900 L826.2 378.4 A540 540 0 0 1 1347.8 518.2 Z"/>
  <path class="sector sector--supply" d="M966 900 L446.3 1419.7 A735 735 0 0 1 257.7 703.6 Z"/>
  <path class="sector sector--capacity" d="M966 900 L1816 900 A850 850 0 0 1 1186 1721 Z"/>

  <!-- core -->
  <circle class="core-gap" cx="966" cy="900" r="196"/>
  <circle class="core-disc" cx="966" cy="900" r="184"/>
  <text class="core-label core-label--equity" x="966" y="840">EQUITY</text>
  <text class="core-label core-label--effectiveness" x="966" y="908">EFFECTIVENESS</text>
  <text class="core-label core-label--efficiency" x="966" y="979">EFFICIENCY</text>

  <!-- demand -->
  <text class="sector-heading" x="872" y="426">DEMAND</text>
  <text class="factor-item" x="875" y="500"><tspan class="num">7</tspan>. Uncertain demand</text>
  <text class="factor-item" x="887" y="545"><tspan class="num">8</tspan>. Limited demand</text>
  <text class="factor-item" x="895" y="591"><tspan class="num">9</tspan>. Client choice</text>
  <text class="factor-item" x="898" y="637"><tspan class="num">10</tspan>. Food wastage</text>

  <!-- supply -->
  <text class="sector-heading" x="336" y="848">SUPPLY</text>
  <text class="factor-item" x="246" y="922"><tspan class="num">1</tspan>. Uncertain material supply</text>
  <text class="factor-item" x="251" y="968"><tspan class="num">2</tspan>. Uncertain monetary supply</text>
  <text class="factor-item" x="255" y="1013"><tspan class="num">3</tspan>. Limited food supply</text>
  <text class="factor-item" x="265" y="1059"><tspan class="num">4</tspan>. Perishability</text>
  <text class="factor-item" x="277" y="1104"><tspan class="num">5</tspan>. Donor constraints</text>
  <text class="factor-item" x="293" y="1150"><tspan class="num">6</tspan>. Donor relationships</text>

  <!-- capacity -->
  <text class="sector-heading" x="1330" y="943">CAPACITY</text>
  <text class="factor-item" x="1140" y="1018"><tspan class="num">11</tspan>. Storage:  <tspan class="num">a</tspan>) Cold</text>
  <text class="factor-item" x="1395" y="1064"><tspan class="num">b</tspan>) Warehouse</text>
  <text class="factor-item" x="1088" y="1118"><tspan class="num">12</tspan>. Transportation</text>
  <text class="factor-item" x="1066" y="1172"><tspan class="num">13</tspan>. Workforce:  <tspan class="num">a</tspan>) Volunteers</text>
  <text class="factor-item" x="1328" y="1218"><tspan class="num">b</tspan>) Expertise</text>
  <text class="factor-item" x="1306" y="1264"><tspan class="num">c</tspan>) Attitudes and Beliefs</text>
  <text class="factor-item" x="1282" y="1309"><tspan class="num">d</tspan>) Collaboration</text>
  <text class="factor-item" x="1255" y="1355"><tspan class="num">e</tspan>) Executive Support</text>
  <text class="factor-item" x="1122" y="1409"><tspan class="num">14</tspan>. External stakeolders</text>
  <text class="factor-item" x="1138" y="1463"><tspan class="num">15</tspan>. Budget</text>
</svg>
</body>
</html>
```